M25 Billboard Advert Required Please

I need an advert for a motorway Billboard on the M25 , the advert should show the following in big letters:
GUTTER CLEANING
TOMSDRAINWORKS.NET and a small logo off to the side (Our logo is attached)

The printer has requested the following (Important please) the advert has to be
pdf file / 300 dpi/landscape orientation / scaled to a minimum 25% advert size ( this particular site is 22ft x 10ft so 25% of this please). Please also make sure that the artwork is embedded and outlined correctly if this is incorrect it will affect the printing of the banner.
Updates

Need extra days to review

Target Market(s)

General Public

Industry/Entity Type

Gutter Cleaning

Requirements
Should not have
• No Change to our Logo

```html
<!DOCTYPE html>
<html lang="en">
<head>
<meta charset="utf-8">
<title>Gutter Cleaning Billboard</title>
<link rel="stylesheet" href="https://fonts.googleapis.com/css2?family=Montserrat:wght@500;600;700;800;900&family=Open+Sans:wght@700&display=swap">
<style>
  :root {
    --page-bg: #b9b9b9;
    --board-black: #0b0c0d;
    --brand-red: #e10e0e;
    --deep-red: #a30000;
    --white: #ffffff;
    --light-grey: #e9eaea;
    --ink: #1a1a1a;
    --photo-teal: #2e4644;
    --photo-dark: #18201f;
    --photo-gutter: #8a8f8b;
  }
  * { margin: 0; padding: 0; box-sizing: border-box; }
  html, body { width: 976px; height: 1200px; overflow: hidden; }
  body { background: var(--page-bg); font-family: "Montserrat", sans-serif; }

  .billboard {
    position: absolute; left: 38px; top: 396px;
    width: 900px; height: 408px;
    background: var(--board-black);
    overflow: hidden;
    box-shadow: 0 6px 18px rgba(0,0,0,.35);
  }
  .hero-photo {
    position: absolute; left: 372px; top: 0; width: 528px; height: 313px;
    background:
      linear-gradient(90deg, var(--board-black) 0%, rgba(11,12,13,0) 38%),
      linear-gradient(180deg, rgba(0,0,0,0) 70%, rgba(11,12,13,.6) 100%),
      linear-gradient(172deg, var(--photo-dark) 0%, var(--photo-teal) 35%, #26393a 62%, var(--photo-gutter) 80%, #2a2e2d 100%);
  }
  .headline {
    position: absolute; left: 35px; font-weight: 900; font-size: 84px;
    line-height: 1; letter-spacing: -1px;
    -webkit-background-clip: text; background-clip: text; color: transparent;
  }
  .headline-gutter {
    top: 30px;
    background-image: linear-gradient(180deg, #ff2a1e 0%, var(--brand-red) 50%, var(--deep-red) 100%);
  }
  .headline-cleaning {
    top: 112px;
    background-image: linear-gradient(180deg, #ffffff 0%, #f2f2f2 50%, #a9a9a9 100%);
  }
  .quote-label {
    position: absolute; left: 39px; top: 212px;
    font-weight: 800; font-size: 23px; color: var(--white); letter-spacing: .2px;
  }
  .quote-label .accent { color: var(--brand-red); }
  .phone {
    position: absolute; left: 35px; top: 244px;
    display: flex; align-items: center; gap: 8px;
    font-weight: 800; font-size: 40px; color: var(--white); line-height: 1;
  }
  .phone svg { width: 30px; height: 30px; flex: none; }

  .footer-shapes { position: absolute; left: 0; top: 313px; width: 900px; height: 95px; }

  .brand {
    position: absolute; left: 35px; top: 338px;
    font-weight: 700; font-size: 23px; color: var(--ink); letter-spacing: -.3px;
  }
  .tagline {
    position: absolute; left: 35px; top: 372px;
    font-family: "Open Sans", sans-serif; font-weight: 700; font-size: 12.5px; color: #2a2a2a;
  }
  .contact-line {
    position: absolute; left: 336px; top: 364px;
    display: flex; align-items: center; gap: 5px;
    font-weight: 500; font-size: 19px; color: var(--white); white-space: nowrap;
  }
  .contact-line .accent { color: var(--brand-red); font-weight: 600; }
  .contact-line svg { width: 15px; height: 15px; flex: none; }
  .contact-line .divider { margin: 0 3px; }
</style>
</head>
<body>
  <div class="billboard">
    <div class="hero-photo" role="img" aria-label="Photo of a worker in yellow gloves clearing leaves from a roof gutter"></div>

    <div class="headline headline-gutter">GUTTER</div>
    <div class="headline headline-cleaning">CLEANING</div>

    <div class="quote-label">REQUEST <span class="accent">A FREE QUOTE:</span></div>
    <div class="phone">
      <svg viewBox="0 0 30 30" aria-hidden="true">
        <circle cx="15" cy="15" r="15" fill="var(--brand-red)"/>
        <path d="M10.5 7.5c.8-.4 1.6 0 2 .8l1.2 2.6c.3.7.1 1.4-.5 1.9l-1 .8c.8 1.8 2.2 3.2 4 4l.8-1c.5-.6 1.2-.8 1.9-.5l2.6 1.2c.8.4 1.2 1.2.8 2l-.6 1.3c-.5 1-1.6 1.6-2.7 1.4-5-1-9-5-10-10-.2-1.1.4-2.2 1.4-2.7z" fill="#fff"/>
        <path d="M17 8.5a5 5 0 0 1 4.5 4.5M17 5.5a8 8 0 0 1 7.5 7.5" stroke="#fff" stroke-width="1.5" fill="none" stroke-linecap="round"/>
      </svg>
      0800 015 7391
    </div>

    <svg class="footer-shapes" viewBox="0 0 900 95" aria-hidden="true">
      <rect x="0" y="0" width="900" height="11" fill="var(--light-grey)"/>
      <rect x="0" y="11" width="900" height="84" fill="var(--board-black)"/>
      <polygon points="0,0 346,0 346,10 262,95 0,95" fill="var(--light-grey)"/>
      <polygon points="317,11 346,11 304,66 286,66" fill="var(--brand-red)"/>
    </svg>

    <div class="brand">Tom's Drainworks</div>
    <div class="tagline">Clean gutters protect your property</div>

    <div class="contact-line">
      <svg viewBox="0 0 16 16" aria-hidden="true">
        <circle cx="8" cy="8" r="7" fill="var(--brand-red)"/>
        <g stroke="#fff" stroke-width=".9" fill="none">
          <circle cx="8" cy="8" r="4.6"/><ellipse cx="8" cy="8" rx="2" ry="4.6"/>
          <line x1="3.4" y1="8" x2="12.6" y2="8"/>
        </g>
      </svg>
      <span>www.<span class="accent">tomsdrainworks</span>.net</span>
      <span class="divider">|</span>
      <svg viewBox="0 0 16 16" aria-hidden="true">
        <circle cx="8" cy="8" r="7" fill="var(--brand-red)"/>
        <rect x="4" y="5.2" width="8" height="5.6" fill="#fff"/>
        <path d="M4 5.4 8 8.6l4-3.2" stroke="var(--brand-red)" stroke-width=".9" fill="none"/>
      </svg>
      <span>info@<span class="accent">tomsdrainworks</span>.net</span>
    </div>
  </div>
</body>
</html>
```